Shareworthy Infographic For Solopreneurs / Business Owners

I would like you to create an infographic for my "10 Steps to Building an Online Business You Can Be Proud Of" content.

STYLE REFERENCE:
Here are my 3 favorite infographics which I would like you to model....

My favorite: http://marlowsglowguideandnotes.example/12-amazing-beauty-benefits-of-honey-infographic/

My 2nd favorite: http://www.inkwrightly.example/grammar-goofs/

My 3rd favorite: http://dwelverde.example/infographic-8-unusual-ways-to-show-off-your-indoor-plants/

BRANDING COLORS TO USE:
Here are my branding colors (hex codes):
I. Primary
-blue
-#002b5c
II. Secondary
-gray
-#afb7bc
III. Tertiary
-green
-#7bc142
I like to use green to emphasize points and "pop out".

CONTENTS OF THE INFOGRAPHIC

10 Steps to Building an Online Business You Can Be Proud Of

1. Pray
Ask God to guide you and let Him know that you are ready, willing, and able to change paths, if He makes it clear to you. Proverbs 16:9 says, we can make our plans, but the LORD determines our steps.

2. Why
Ask yourself "why" you are doing this. Leverage your goals and dreams to pull you towards success. Place pictures on your desktop or other places you will see them regularly.

3. Avatar
Picture yourself in a desperate time in life. The people who you can serve now are going through that. Create your products, services, content, and copy to "speak" to 1 specific avatar (YOU; in that time of desperation).

4. Commit
"How" you will serve your avatar is yet to be discovered. If you are "half in", your avatar will continue to suffer. Commit at least 10 hours per week to building this business, for the next 12 months... and don't expect to be profitable in the first few months.

5. Model
Pick 1 "guru" to model. If you attempt to do this on your own, with no mentohrship, your probability of failure is higher because mistakes can be costly. On the other hand, if you pick too many "gurus" to follow, your probability of failure is also high because you develop "shiny object syndrome".

6. Ask
Before you create a product or service, ask your audience what their biggest challenge is, to affirm that your idea is in demand.

7. Specialize
Read a few books, watch training videos, and do research online to become a specialist in your area. For example, if you believe that TallyNest would have been the solution to your "desperate time in life", spend a few dozen hours learning about it so that you can teach your audience the shortcut to success in TallyNest. If you have already mastered TallyNest (for example), you can skip this step.

8. Creation
Create a mini-version of your product/service and offer it for less money. About 1 in 10 product/service ideas succeed. Do not spend a lot of time creating your product/service until you KNOW it is in demand. To find out, write a blog post that dives deep on 1 of the topics of your product/service and points them to your solution. If you are getting a lot of engagement, that is a good sign.

9. Launch
Advertise your blog post on Chatterbay and target fans of a thought leader that your avatar would be following because of this challenge. For example, someone looking to get out of debt may have liked Glen Worthby's page.

10. Nurture
Keep a database of prospects and customers. Create new content, new products, new services, and point them to good resources to nurture the relationship and make money.

FOR MORE INFORMATION ABOUT MY COMPANY:
Please visit my website: http://leadbrook.example/

Thanks much!

Owen Pellow

Project Deadline Extended Reason: Thank you for your interest in my infographic job. I have had a request to extend the deadline. Added Wednesday, May 18, 2016

Thank you for all your submission! Here are some helpful information that may give a bit of clarity: - Illustration of a person is preferred over a photo or real images; can be cartoony, semi-real, open to any illustration style - I'd rather see the image of the person be used less and instead use colorful images of objects, symbols, etc.. that appeals to the emotion and tells the story of the situation. Similar to the infographic found here: http://marlowsglowguideandnotes.example/12-amazing-beauty-benefits-of-honey-infographic/ Notice how different images were used in some of the items rather than showing a person to explain the content. The contest will be extended for another round! Looking forward to your new submissions, Thanks again!

Target Market(s)

Solopreneurs who have "shiny object syndrome"

Industry/Entity Type

Business

Font styles to use
Sans Serif
Other font styles liked:
• Arial Bold

Requirements
Must have
• exciting, captivating, sharp, contrasting colors
Nice to have
• A couple images of frustrated, confused, depressed men. Here are some examples...
• http://files.clipvault.example/users/owenpellow/folders/Grabbit/media/a92f7c03-f690-4f41-adf8-adfa71ba846c/05.15.2016-10.34.png
• And if possible, a happy, successful, and relieved man at the end of the infographic.
• Prefer illustrations over photographs or real images.
Should not have
• women, kids, business suits, tattoos, wild people.... just the average man who is trying to start a business and is frustrated but wants mental relief.

```html
<!DOCTYPE html>
<html lang="en">
<head>
<meta charset="utf-8">
<title>10 Steps to Building an Online Business You Can Be Proud Of</title>
<link rel="stylesheet" href="https://fonts.googleapis.com/css2?family=Anton&family=Arimo:wght@400;700&display=swap">
<style>
  :root{
    --navy:#0a2a62;
    --navy-deep:#06204f;
    --gray:#afb7bc;
    --gray-dark:#8a949b;
    --green:#7bc142;
    --white:#ffffff;
  }
  *{margin:0;padding:0;box-sizing:border-box}
  html,body{width:1200px;height:3600px;overflow:hidden}
  body{
    position:relative;
    background:linear-gradient(180deg,var(--navy) 0%,var(--navy-deep) 100%);
    font-family:"Arimo",Arial,sans-serif;
    color:var(--white);
  }
  .photo{position:absolute}
  .photo-frustrated{left:0;top:0;width:312px;height:900px;
    background:linear-gradient(180deg,#e9ecef 0%,#cfd6dc 40%,#2b2f36 60%,#1a1d22 100%);
    border-radius:0 0 40px 0;opacity:.95}
  .photo-happy{left:796px;top:2544px;width:396px;height:1056px;
    background:linear-gradient(180deg,#4b3a30 0%,#3a3f48 30%,#1c1f25 100%);
    border-radius:60px 60px 0 0;opacity:.95}

  .title-number{position:absolute;left:462px;top:20px;width:156px;height:156px;border-radius:50%;
    background:var(--gray);border:8px solid var(--gray-dark);box-shadow:0 0 0 6px rgba(255,255,255,.5);
    font-family:"Anton",Impact,sans-serif;font-size:100px;line-height:140px;text-align:center;color:var(--white)}
  .title-steps{position:absolute;left:624px;top:0;font-family:"Anton",Impact,sans-serif;font-size:160px;line-height:190px;letter-spacing:4px}
  .title-line{position:absolute;display:block;left:330px;width:860px;font-family:"Anton",Impact,sans-serif;
    text-align:center;text-transform:uppercase;white-space:nowrap;font-weight:400}
  .title-line.sub{top:222px;font-size:62px;line-height:76px;letter-spacing:0}
  .title-line.main{top:292px;font-size:92px;line-height:108px;letter-spacing:1px}
  .pop{color:var(--green)}

  .badge{position:absolute;width:150px;height:150px;border-radius:50%;
    background:var(--gray);border:9px solid var(--gray-dark);box-shadow:0 0 0 6px rgba(255,255,255,.55);
    font-family:"Anton",Impact,sans-serif;font-size:96px;line-height:132px;text-align:center;color:var(--white)}

  .step{position:absolute}
  .step h2{font-family:"Arimo",Arial,sans-serif;font-weight:700;font-size:48px;line-height:54px;letter-spacing:1px;margin-bottom:4px}
  .step p{font-size:26.5px;line-height:37px}
  .step.right{text-align:right}
  .hl{color:var(--green)}

  .footer-name{position:absolute;left:168px;top:3340px;width:760px;text-align:center;
    font-family:"Anton",Impact,sans-serif;font-size:176px;line-height:200px;letter-spacing:14px;color:var(--white)}
</style>
</head>
<body>
  <div class="photo photo-frustrated" role="img" aria-label="Frustrated man in white shirt and tie holding his head"></div>
  <div class="photo photo-happy" role="img" aria-label="Happy, relieved man raising his fists in celebration"></div>

  <header>
    <div class="title-number">10</div>
    <div class="title-steps">STEPS</div>
    <h1>
      <span class="title-line sub">To building an online business</span>
      <span class="title-line main">You can be <span class="pop">proud</span> of</span>
    </h1>
  </header>

  <div class="badge" style="left:155px;top:458px">1</div>
  <section class="step" style="left:384px;top:420px;width:790px">
    <h2>PRAY</h2>
    <p>Ask God to guide you and let Him know that you are <span class="hl">ready, willing, and able to change paths</span>, if He makes it clear to you. Proverbs 16:9 says, we can make our plans, but the LORD determines our steps.</p>
  </section>

  <div class="badge" style="left:1029px;top:681px">2</div>
  <section class="step right" style="right:200px;top:680px;width:840px">
    <h2>WHY</h2>
    <p>Ask yourself "why" you are doing this. <span class="hl">Leverage your goals and dreams to pull you towards success.</span> Place pictures on your desktop or other places you will see them regularly.</p>
  </section>

  <div class="badge" style="left:155px;top:909px">3</div>
  <section class="step" style="left:384px;top:884px;width:800px">
    <h2>AVATAR</h2>
    <p>Picture yourself in a desperate time in life. The people who you can <span class="hl">serve</span> now are going through that. Create your products, services, content, and copy to "speak" to 1 specific avatar (YOU; in that time of desperation).</p>
  </section>

  <div class="badge" style="left:1017px;top:1245px">4</div>
  <section class="step right" style="right:235px;top:1170px;width:945px">
    <h2>COMMIT</h2>
    <p>"How" you will serve your avatar is yet to be discovered. If you are "half in", your avatar will continue to suffer. <span class="hl">Commit</span> at least 10 hours per week to building this business, for the next 12 months... and don't expect to be profitable in the first few months.</p>
  </section>

  <div class="badge" style="left:21px;top:1461px">5</div>
  <section class="step" style="left:200px;top:1484px;width:984px">
    <h2>MODEL</h2>
    <p>Pick 1 "guru" to model. If you attempt to do this on your own, with no mentorship, your probability of failure is higher because <span class="hl">mistakes can be costly</span>. On the other hand, if you pick too many "gurus" to follow, your probability of failure is also high because you develop "shiny object syndrome".</p>
  </section>

  <div class="badge" style="left:1029px;top:1749px">6</div>
  <section class="step right" style="right:210px;top:1748px;width:900px">
    <h2>ASK</h2>
    <p>Before you create a product or service, ask your audience what their <span class="hl">biggest challenge</span> is, to affirm that your idea is in demand.</p>
  </section>

  <div class="badge" style="left:21px;top:1989px">7</div>
  <section class="step" style="left:200px;top:1952px;width:984px">
    <h2>SPECIALIZE</h2>
    <p>Read a few books, watch training videos, and do research online to <span class="hl">become a specialist in your area</span>. For example, if you believe that TallyNest would have been the solution to your "desperate time in life", spend a few dozen hours learning about it so that you can teach your audience the shortcut to success in TallyNest. If you have already mastered TallyNest (for example), you can skip this step.</p>
  </section>

  <div class="badge" style="left:1017px;top:2349px">8</div>
  <section class="step right" style="right:215px;top:2288px;width:965px">
    <h2>CREATION</h2>
    <p>Create a mini-version of your product/service and offer it for less money. About 1 in 10 product/service ideas succeed. Do not spend a lot of time creating your product/service until you KNOW it is in demand. To find out, <span class="hl">write a blog post</span> that dives deep on 1 of the topics of your product/service and points them to your solution. If you are getting a lot of engagement, that is a good sign.</p>
  </section>

  <div class="badge" style="left:21px;top:2757px">9</div>
  <section class="step" style="left:200px;top:2732px;width:580px">
    <h2>LAUNCH</h2>
    <p>Advertise your blog post on Chatterbay and <span class="hl">target fans of a thought leader</span> that your avatar would be following because of this challenge. For example, someone looking to get out of debt may have liked Glen Worthby's page.</p>
  </section>

  <div class="badge" style="left:801px;top:3045px">10</div>
  <section class="step right" style="right:425px;top:3070px;width:760px">
    <h2>NURTURE</h2>
    <p>Keep a database of prospects and customers. Create new content, new products, new services, and point them to good resources to nurture the relationship and <span class="hl">make money</span>.</p>
  </section>

  <footer class="footer-name">LEADBROOK</footer>
</body>
</html>
```